Simple but elegant business card/logo design for exclusive beauty business

We need a logo designed for a new elegant and exclusive beauty business called "G". The logo itself should be a stylistic and custom design for the letter "G". We would like the business card to have the logo as the centrepiece on a clean background. Gold Logo on black background or silver on white background.

The business card details should be displayed centre of the card. Details are as follows:

Tamsin Rowe
Facebook: /simplyshinebyr
Instagram: /simplyshinebyr

The words "Simply Shine" should also appear somewhere on the card.

G

• Design must be simple, clean and elegant
• The design should not be cluttered

```html
<!DOCTYPE html>
<html lang="en">
<head>
<meta charset="utf-8">
<title>Simply Shine — Business Card</title>
<link href="https://fonts.googleapis.com/css2?family=Open+Sans:wght@400&family=Raleway:wght@400;600&display=swap" rel="stylesheet">
<style>
  :root {
    --backdrop: #2b2b2b;
    --card: #161616;
    --card-back: #141414;
    --gold: #c9b57a;
    --gold-light: #e4d49c;
    --gold-dark: #9c8a52;
  }
  * { margin: 0; padding: 0; box-sizing: border-box; }
  html, body { width: 1200px; height: 600px; overflow: hidden; }
  body {
    background: var(--backdrop);
    position: relative;
    font-family: "Open Sans", sans-serif;
  }
  .card {
    position: absolute;
    top: 165px;
    width: 465px;
    height: 271px;
    border-radius: 14px;
  }
  .card-front { left: 125px; background: var(--card); }
  .card-back { left: 612px; background: var(--card-back); }

  .tagline {
    position: absolute;
    left: 34px;
    top: 18px;
    font-family: "Raleway", sans-serif;
    font-weight: 400;
    font-size: 22px;
    color: var(--gold);
    letter-spacing: 0.2px;
  }
  .tagline strong { font-weight: 600; }

  .brand-mark {
    position: absolute;
    font-family: "Raleway", sans-serif;
    font-weight: 600;
    color: var(--gold-light);
  }
  .card-front .brand-mark { right: 34px; top: 22px; font-size: 22px; }
  .card-back .brand-mark {
    left: 0; right: 0; top: 50%;
    transform: translateY(-50%);
    text-align: center;
    font-size: 40px;
    letter-spacing: 2px;
  }

  .holder-name {
    position: absolute;
    left: 37px;
    top: 156px;
    font-size: 20px;
    color: var(--gold);
  }
  .name-rule {
    position: absolute;
    left: 37px;
    top: 187px;
    width: 390px;
    height: 2px;
    background: linear-gradient(90deg, var(--gold-dark), var(--gold-light), var(--gold-dark));
  }
  .contact-row {
    position: absolute;
    left: 37px;
    width: 390px;
    display: flex;
    justify-content: space-between;
    font-size: 13px;
    color: var(--gold);
  }
  .contact-row.primary { top: 198px; }
  .contact-row.social { top: 230px; }
  .contact-item { display: flex; align-items: center; gap: 6px; }
  .contact-item svg { display: block; }
  .social-square {
    width: 10px; height: 10px;
    background: var(--gold);
    border-radius: 1px;
  }
</style>
</head>
<body>
  <section class="card card-front">
    <p class="tagline">Simply <strong>Shine</strong></p>
    <p class="brand-mark">Rowe</p>

    <p class="holder-name">Tamsin Rowe</p>
    <div class="name-rule"></div>

    <div class="contact-row primary">
      <span class="contact-item">
        <svg width="12" height="10" viewBox="0 0 12 10" aria-hidden="true">
          <path d="M1 3 Q6 -1 11 3 L10 4.5 L8 4 L8 3 Q6 2 4 3 L4 4 L2 4.5 Z" fill="var(--gold)"/>
          <rect x="2.5" y="5" width="7" height="4.5" rx="0.8" fill="var(--gold)"/>
        </svg>
        000 000 0000
      </span>
      <span class="contact-item">
        hello@simplyshine.co
        <svg width="12" height="9" viewBox="0 0 12 9" aria-hidden="true">
          <rect x="0.5" y="0.5" width="11" height="8" fill="var(--gold)"/>
          <path d="M0.5 0.8 L6 5 L11.5 0.8" fill="none" stroke="var(--card)" stroke-width="1"/>
        </svg>
      </span>
    </div>

    <div class="contact-row social">
      <span class="contact-item"><span class="social-square"></span>/simplyshinebyr</span>
      <span class="contact-item">/simplyshinebyr<span class="social-square"></span></span>
    </div>
  </section>

  <section class="card card-back">
    <p class="brand-mark">Rowe</p>
  </section>
</body>
</html>
```